Seasons Greetings from Brackfold Hire.

Brackfold Hire is a Temporary Structures company based in South East London (South Bermondsey).
We dry hire Brackfold as well as deliver and manage projects with our own crew.
We are looking for someone to design our Christmas card or as I prefer to say ‘Season’s Greetings Card’ as this includes everyone religious or not.
The card should reflect Brackfold Hire Ltd and what we do, if you take a look at our website please look at the hires section only,
http://www.brackfold.co.uk/stage-hire.htm
Also take a look at our Brackfold Video’s
http://www.vidplume.example/user/firstbrackfold?feature=results_main
We would also like the card to be friendly and humorous,
Card Size: 210mm x 297mm folded to 210mm x 148mm
Suggested text for Front of card: Seasons Greetings from Brackfold Hire
Inner Text has yet to be confirmed but something like: Wishing you a Merry Christmas and a Happy New Year from everyone at Brackfold Hire
A clever use of the Brackfold logo or weave of the deck would be proffered. I have attached a PDF of a previous card.
Please DO Not show the Mantis Risers.
Please let me know if you require anymore info,
Target Market(s)
Brackfold Customers
Industry/Entity Type
Religious
Requirements
Must have
- Must be a professional looking card

```html
<!DOCTYPE html>
<html lang="en">
<head>
<meta charset="utf-8">
<title>Seasons Greetings from Brackfold Hire – card spread</title>
<link rel="stylesheet" href="https://fonts.googleapis.com/css2?family=Great+Vibes&family=Open+Sans:wght@400;700&display=swap">
<style>
  :root {
    --page: #ffffff;
    --label: #111111;
    --ink: #ffffff;
    --blue-bright: #1a4aa3;
    --blue-mid: #1b3b8f;
    --navy: #1d2a6c;
    --navy-deep: #1b2462;
    --hill: #1e2b6b;
    --shadow: rgba(0, 0, 0, 0.45);
  }
  * { box-sizing: border-box; margin: 0; padding: 0; }
  html, body {
    width: 1200px; height: 900px; overflow: hidden;
    background: var(--page);
    font-family: "Open Sans", Arial, sans-serif;
  }
  .canvas { position: relative; width: 1200px; height: 900px; }

  .view-label {
    position: absolute; font-size: 16px; color: var(--label);
    transform: translateX(-50%);
  }

  .card {
    position: absolute; top: 116px; width: 487px; height: 684px;
    box-shadow: 3px 4px 6px var(--shadow);
    overflow: hidden;
  }
  .card--outside { left: 105px; }
  .card--inside { left: 626px; }

  .panel { position: absolute; left: 0; width: 100%; height: 342px; }
  .panel--upper { top: 0; }
  .panel--lower { top: 342px; }

  /* Outside: back panel is printed upside down so it reads after folding */
  .back-panel {
    background: linear-gradient(to top, var(--blue-bright) 0%, var(--blue-mid) 45%, var(--navy) 100%);
    transform: rotate(180deg);
    color: var(--ink);
  }
  .back-panel .web-address {
    position: absolute; top: 42px; left: 0; width: 100%;
    text-align: center; font-size: 13px; font-weight: 700; letter-spacing: 6px;
  }
  .brand-mark {
    display: flex; align-items: center; justify-content: center; gap: 8px;
    color: var(--ink); font-family: "Open Sans", Arial, sans-serif; font-weight: 700;
  }
  .brand-mark .brand-square { width: 14px; height: 14px; background: var(--ink); }
  .back-panel .brand-mark {
    position: absolute; top: 150px; left: 0; width: 100%; font-size: 24px; letter-spacing: 1px;
  }
  .office-list {
    position: absolute; top: 268px; left: 30px; right: 30px;
    display: flex; justify-content: space-between;
  }
  .office { font-size: 5.8px; line-height: 9.5px; font-style: normal; text-align: left; }
  .office strong { font-weight: 700; }

  .front-panel {
    background: linear-gradient(to bottom, var(--navy) 0%, var(--blue-mid) 30%, var(--blue-bright) 60%, var(--blue-mid) 100%);
  }
  .front-panel svg, .inside-lower svg { position: absolute; inset: 0; }
  .front-greeting {
    position: absolute; top: 286px; left: 0; width: 100%;
    text-align: center; color: var(--ink);
    font-family: "Great Vibes", cursive; font-size: 20px;
  }

  /* Inside */
  .inside-upper {
    background: linear-gradient(to bottom, var(--navy-deep) 0%, var(--navy) 50%, var(--blue-mid) 100%);
    color: var(--ink); text-align: center;
  }
  .inside-upper .brand-mark {
    position: absolute; top: 66px; left: 0; width: 100%; font-size: 26px;
  }
  .inside-message {
    position: absolute; top: 152px; left: 0; width: 100%;
    font-family: "Great Vibes", cursive; font-weight: 400; line-height: 1;
  }
  .inside-message .line { display: block; }
  .inside-message .line--small { font-size: 27px; margin-bottom: 6px; }
  .inside-message .line--large { font-size: 39px; margin-bottom: 2px; }
  .inside-message .line--joiner { font-size: 23px; margin-bottom: 4px; }

  .inside-lower {
    background: linear-gradient(to bottom, var(--blue-mid) 0%, var(--blue-bright) 60%, var(--blue-mid) 100%);
  }
</style>
</head>
<body>
<main class="canvas">
  <span class="view-label" style="left:347px; top:87px;">Back</span>
  <span class="view-label" style="left:869px; top:87px;">Inside open</span>
  <span class="view-label" style="left:347px; top:813px;">Front</span>

  <section class="card card--outside" aria-label="Outside of card">
    <div class="panel panel--upper back-panel">
      <p class="web-address">WWW.BRACKFOLD.CO.UK</p>
      <div class="brand-mark"><span class="brand-square"></span><span>BRACKFOLD</span></div>
      <div class="office-list">
        <address class="office"><strong>BRACKFOLD RENTALS</strong><br>Unit 4 Dockside Yard,<br>12 Marsh Lane, London,<br>SE16 2XA<br>t: 020 7946 0123<br>e: rentals@brackfold.co.uk</address>
        <address class="office"><strong>BRACKFOLD SALES</strong><br>18 Quay Road,<br>Deptwell, London,<br>SE8 4QP<br>t: 020 7946 0456<br>e: info@brackfold.co.uk</address>
        <address class="office"><strong>NORTHERN SALES OFFICE</strong><br>9 Mill Street, Northam,<br>Chesford,<br>CW5 7RT<br>t: 01632 960 271<br>e: north@brackfold.co.uk</address>
        <address class="office"><strong>BRACKFOLD NY INC</strong><br>88 Harbor St,<br>Brooklyn,<br>NY 11200<br>t: (555) 010-2200<br>www.brackfoldny.example</address>
        <address class="office"><strong>BRACKFOLD INC</strong><br>410 Exhibit Pl,<br>Los Angeles,<br>CA 90000<br>t: (555) 010-4400<br>www.brackfold.example</address>
      </div>
    </div>

    <div class="panel panel--lower front-panel">
      <svg width="487" height="342" viewBox="0 0 487 342">
        <defs>
          <radialGradient id="treeToneFront" cx="50%" cy="50%" r="50%">
            <stop offset="0%" stop-color="#ffffff" stop-opacity="0.7"/>
            <stop offset="55%" stop-color="#ffffff" stop-opacity="0.3"/>
            <stop offset="100%" stop-color="#ffffff" stop-opacity="0"/>
          </radialGradient>
          <radialGradient id="skyHazeFront" cx="50%" cy="50%" r="50%">
            <stop offset="0%" stop-color="#c9d6ff" stop-opacity="0.22"/>
            <stop offset="100%" stop-color="#c9d6ff" stop-opacity="0"/>
          </radialGradient>
          <radialGradient id="hillGlowFront" cx="50%" cy="30%" r="55%">
            <stop offset="0%" stop-color="#3f5fc0" stop-opacity="0.8"/>
            <stop offset="100%" stop-color="#3f5fc0" stop-opacity="0"/>
          </radialGradient>
        </defs>
        <ellipse role="img" aria-label="Night sky scattered with white twinkling stars" cx="243" cy="80" rx="240" ry="70" fill="url(#skyHazeFront)"/>
        <path d="M0 139 Q243 20 487 128" fill="none" stroke="#ffffff" stroke-width="2"/>
        <path d="M0 235 Q243 195 487 230 L487 342 L0 342 Z" fill="var(--hill)"/>
        <ellipse cx="243" cy="250" rx="180" ry="60" fill="url(#hillGlowFront)"/>
        <g role="img" aria-label="Row of Christmas trees built from white truss frames on a hill" fill="url(#treeToneFront)">
          <ellipse cx="70" cy="210" rx="10" ry="16"/>
          <ellipse cx="110" cy="192" rx="22" ry="40"/>
          <ellipse cx="145" cy="214" rx="10" ry="16"/>
          <ellipse cx="200" cy="191" rx="42" ry="76"/>
          <ellipse cx="250" cy="212" rx="10" ry="16"/>
          <ellipse cx="300" cy="196" rx="34" ry="62"/>
          <ellipse cx="365" cy="205" rx="16" ry="28"/>
          <ellipse cx="412" cy="212" rx="10" ry="16"/>
        </g>
      </svg>
      <p class="front-greeting">Seasons Greetings from Brackfold Hire</p>
    </div>
  </section>

  <section class="card card--inside" aria-label="Inside of card">
    <div class="panel panel--upper inside-upper" role="img" aria-label="Starry night sky">
      <div class="brand-mark"><span class="brand-square"></span><span>BRACKFOLD</span></div>
      <h1 class="inside-message">
        <span class="line line--small">Wishes You a</span>
        <span class="line line--large">Merry Christmas</span>
        <span class="line line--joiner">And a</span>
        <span class="line line--large">Happy New Year</span>
      </h1>
    </div>

    <div class="panel panel--lower inside-lower">
      <svg width="486" height="342" viewBox="0 0 486 342">
        <defs>
          <radialGradient id="treeToneInside" cx="50%" cy="50%" r="50%">
            <stop offset="0%" stop-color="#ffffff" stop-opacity="0.7"/>
            <stop offset="55%" stop-color="#ffffff" stop-opacity="0.3"/>
            <stop offset="100%" stop-color="#ffffff" stop-opacity="0"/>
          </radialGradient>
          <radialGradient id="sleighTone" cx="50%" cy="50%" r="50%">
            <stop offset="0%" stop-color="#ffffff" stop-opacity="0.75"/>
            <stop offset="100%" stop-color="#ffffff" stop-opacity="0"/>
          </radialGradient>
          <radialGradient id="skyHazeInside" cx="50%" cy="50%" r="50%">
            <stop offset="0%" stop-color="#c9d6ff" stop-opacity="0.2"/>
            <stop offset="100%" stop-color="#c9d6ff" stop-opacity="0"/>
          </radialGradient>
          <radialGradient id="hillGlowInside" cx="50%" cy="30%" r="55%">
            <stop offset="0%" stop-color="#3f5fc0" stop-opacity="0.8"/>
            <stop offset="100%" stop-color="#3f5fc0" stop-opacity="0"/>
          </radialGradient>
        </defs>
        <ellipse role="img" aria-label="Night sky scattered with white twinkling stars" cx="140" cy="120" rx="140" ry="60" fill="url(#skyHazeInside)"/>
        <path d="M0 152 Q150 72 272 62" fill="none" stroke="#ffffff" stroke-width="2"/>
        <ellipse role="img" aria-label="White silhouette of a sleigh pulled by reindeer" cx="349" cy="62" rx="78" ry="14" fill="url(#sleighTone)"/>
        <path d="M0 238 Q243 195 486 230 L486 342 L0 342 Z" fill="var(--hill)"/>
        <ellipse cx="243" cy="262" rx="180" ry="60" fill="url(#hillGlowInside)"/>
        <g role="img" aria-label="Row of Christmas trees built from white truss frames on a hill" fill="url(#treeToneInside)">
          <ellipse cx="67" cy="211" rx="10" ry="16"/>
          <ellipse cx="109" cy="200" rx="20" ry="40"/>
          <ellipse cx="145" cy="200" rx="10" ry="18"/>
          <ellipse cx="192" cy="212" rx="36" ry="64"/>
          <ellipse cx="236" cy="200" rx="8" ry="12"/>
          <ellipse cx="266" cy="200" rx="9" ry="15"/>
          <ellipse cx="304" cy="215" rx="42" ry="76"/>
          <ellipse cx="342" cy="205" rx="8" ry="12"/>
          <ellipse cx="369" cy="212" rx="20" ry="40"/>
          <ellipse cx="392" cy="210" rx="8" ry="12"/>
          <ellipse cx="418" cy="215" rx="9" ry="16"/>
        </g>
      </svg>
    </div>
  </section>
</main>
</body>
</html>
```